Ridgecrest Casino poster and artwork for the 48th Falcon Crown Stakes

Ridgecrest Casino hosts the Falcon Crown Stakes each year. The derby purse is $750,000 and we are Grade III this year. The derby date is August 5, 2017 with the post time at 2pm.

Once the artwork is selected we will use it for posters, invites, e-blasts, website etc.

I have attached the artwork from 2016 as an example. The logo must be included in the artwork and it is also attached

Industry/Entity Type

Casino

Font styles to use
Sans Serif

Requirements
Must have
• West Virginia logo (attached)
• Date-August 5, 2017
• First post time at 2pm
• Ridgecrest Casino (logo attached)

```html
<!DOCTYPE html>
<html lang="en">
<head>
<meta charset="utf-8">
<title>Falcon Crown Stakes – 48th Running</title>
<link href="https://fonts.googleapis.com/css2?family=Bebas+Neue&family=Oswald:wght@400;500&family=Roboto:wght@400&display=swap" rel="stylesheet">
<style>
  :root {
    --sage-dark: #7b8469;
    --sage: #9aa38a;
    --mist: #e9ebe0;
    --band: #8a957c;
    --display: #5f6a4d;
    --line: #6f7a5e;
    --white: #ffffff;
    --photo-warm: rgba(164, 88, 48, 0.5);
    --photo-soft: rgba(164, 88, 48, 0.18);
  }
  * { margin: 0; padding: 0; box-sizing: border-box; }
  html, body { width: 849px; height: 1200px; overflow: hidden; background: var(--sage); }
  .poster {
    position: relative;
    width: 849px;
    height: 1200px;
    overflow: hidden;
    font-family: "Oswald", sans-serif;
    color: var(--white);
    background:
      radial-gradient(ellipse 360px 330px at 424px 600px, var(--mist) 0%, rgba(233,235,224,0.8) 40%, rgba(233,235,224,0) 100%),
      radial-gradient(ellipse 560px 700px at 50% 50%, var(--sage) 40%, var(--sage-dark) 100%);
  }
  .frame {
    position: absolute;
    inset: 12px;
    border: 1.5px solid rgba(255,255,255,0.35);
  }
  .event-mark {
    position: absolute;
    top: 100px;
    left: 0;
    width: 100%;
    text-align: center;
    font-weight: 500;
    font-size: 44px;
    letter-spacing: 3px;
    line-height: 1.05;
  }
  .hero-photo {
    position: absolute;
    left: 170px;
    top: 285px;
    width: 410px;
    height: 430px;
    background: radial-gradient(ellipse 50% 48% at 55% 40%, var(--photo-warm) 0%, var(--photo-soft) 55%, rgba(164,88,48,0) 100%);
  }
  .ribbon { position: absolute; left: 118px; top: 600px; }
  .title {
    position: absolute;
    top: 526px;
    left: 0;
    width: 100%;
    text-align: center;
    font-family: "Bebas Neue", sans-serif;
    font-weight: 400;
    font-size: 218px;
    line-height: 1;
    letter-spacing: 2px;
    color: var(--display);
    opacity: 0.9;
  }
  .running {
    position: absolute;
    top: 710px;
    width: 100%;
    text-align: center;
    font-weight: 500;
    font-size: 54px;
    line-height: 1;
  }
  .divider { position: absolute; left: 144px; }
  .divider--top { top: 794px; }
  .divider--bottom { top: 928px; }
  .date {
    position: absolute;
    top: 820px;
    width: 100%;
    text-align: center;
    font-weight: 500;
    font-size: 54px;
    line-height: 1;
  }
  .post-time {
    position: absolute;
    top: 880px;
    width: 100%;
    text-align: center;
    font-weight: 500;
    font-size: 34px;
    line-height: 1;
  }
  .host {
    position: absolute;
    top: 1020px;
    width: 100%;
    text-align: center;
    font-weight: 500;
    line-height: 1;
  }
  .host__name { display: block; font-size: 44px; letter-spacing: 2px; }
  .host__type { display: block; font-size: 30px; letter-spacing: 2px; margin-top: 2px; }
  .host__tagline { display: block; font-size: 12px; letter-spacing: 3px; margin-top: 6px; }
  .parent-brand {
    position: absolute;
    top: 1122px;
    width: 100%;
    display: flex;
    justify-content: center;
    align-items: center;
    gap: 8px;
    font-weight: 500;
    font-size: 19px;
    letter-spacing: 2px;
    line-height: 1;
  }
  .parent-brand__square { width: 15px; height: 15px; background: var(--white); }
  .partner-badge {
    position: absolute;
    left: 28px;
    top: 1126px;
    width: 48px;
    height: 48px;
    border-radius: 6px;
    border: 1.5px solid rgba(255,255,255,0.7);
  }
  .disclaimer {
    position: absolute;
    top: 1162px;
    width: 100%;
    text-align: center;
    font-family: "Roboto", sans-serif;
    font-weight: 400;
    font-size: 11px;
    letter-spacing: 0.2px;
  }
</style>
</head>
<body>
<main class="poster">
  <div class="frame"></div>

  <div class="event-mark">FALCON CROWN<br>STAKES</div>

  <div class="hero-photo" role="img" aria-label="Photo of a jockey in black and yellow silks riding a chestnut racehorse through dust"></div>

  <svg class="ribbon" width="614" height="80" viewBox="0 0 614 80">
    <polygon points="0,0 110,0 110,80 0,80 22,40" fill="var(--band)"/>
    <polygon points="614,0 504,0 504,80 614,80 592,40" fill="var(--band)"/>
  </svg>

  <h1 class="title">DERBY</h1>
  <p class="running">48TH RUNNING</p>

  <svg class="divider divider--top" width="560" height="12" viewBox="0 0 560 12">
    <line x1="0" y1="6" x2="268" y2="6" stroke="var(--line)" stroke-width="2"/>
    <line x1="292" y1="6" x2="560" y2="6" stroke="var(--line)" stroke-width="2"/>
    <polygon points="280,0 288,6 280,12 272,6" fill="var(--line)"/>
  </svg>

  <p class="date">AUGUST 5, 2017</p>
  <p class="post-time">FIRST POST TIME AT 2PM</p>

  <svg class="divider divider--bottom" width="560" height="12" viewBox="0 0 560 12">
    <line x1="0" y1="6" x2="268" y2="6" stroke="var(--line)" stroke-width="2"/>
    <line x1="292" y1="6" x2="560" y2="6" stroke="var(--line)" stroke-width="2"/>
    <polygon points="280,0 288,6 280,12 272,6" fill="var(--line)"/>
  </svg>

  <p class="host">
    <span class="host__name">RIDGECREST</span>
    <span class="host__type">CASINO</span>
    <span class="host__tagline">RACETRACK &amp; RESORT</span>
  </p>

  <p class="parent-brand"><span class="parent-brand__square"></span>SUMMITVIEW RESORTS</p>

  <div class="partner-badge"></div>

  <p class="disclaimer">Ridgecrest reserves all rights to change or cancel any information at anytime without prior notice.</p>
</main>
</body>
</html>
```